Occupational Therapy promotional poster

We need 2 x A4 posters to be created:
- 1 with a male super hero
- 1 with a female super hero (see suggested design).

These posters will be used for a promotional campaign celebrating occupational therapy. The idea being that occupational therapists are our local superhero. We see them as the ‘unsung heroes’ of our local communities, so this campaign is a play on that idea.

These posters will be displayed on community notice boards and in hospitals. They will also be used on display tables promoting what occupational therapy is. They will also potentially be used as handouts in presentations. We plan to use these posters for the coming 2 years.

As these will be displayed on noticeboards they need to be bright and colourful. The colours suggested in the attachment are the types of colours we would like used (blue, yellow and red).

We envision these posters being displayed side by side.

Although we are open to interpretation of the “super hero” theme – we particularly liked the black super hero images as they look similar to the symbol for wheelchair access (which occupational therapists use).

Alternatively, a comic book inspired design would also be appealing – see inspiration images in attached document.

See the images that we have drawn inspiration from. I've included the black generic super heroes as well as the comic book style.

This design needs to include the KLRV-PTB logo which is included.

The superhero also needs to have a starwarden style logo somewhere visable. This could be on their chest or on their cape – depending on their angle. Instead of the Starwarden ‘S’, please put ‘OT’.

The content for both posters is identical. However, we would like 1 male version of the poster and 1 female version of the poster.

The superhero graphic needs to be G-rated. For the female graphic - it cannot include cleavage or clothing that is too tight/revealing.

Based on the locations where the poster will be displayed, it does need to have a professional feel.

ATTACHED:
- the KLRV-PTB Logo (to be included)
- a design brief + all text that needs to be included
- an example of the type of posters that we are envisioning

Target Market(s)

General public in New Zealand: Patients in hospital waiting rooms, mothers of children in childcare, elderly people who look at notice boards

Industry/Entity Type

Health Care

Font styles to use
Sans Serif

Requirements
Must have
• 2 A4 twin posters. Identical content but 1 female version and 1 male version
• The KLRV-PTB logo (attached)
• A "superhero" symbol on the chest or cape of the superhero. It should look like the starwarden symbol but instead say "OT" rather than S.
• Must be bright and colourful
• Must include all text included
Should not have
• Any nudity, revealing poses or tight clothing. G-rated.

```html
<!DOCTYPE html>
<html lang="en">
<head>
<meta charset="utf-8">
<title>Meet Your Local Superhero – The Occupational Therapist</title>
<link rel="stylesheet" href="https://fonts.googleapis.com/css2?family=Roboto+Condensed:ital,wght@0,700;0,900;1,700;1,900&family=Open+Sans:wght@400;600;700&display=swap">
<style>
  :root {
    --red: #d7261e;
    --red-deep: #b51a15;
    --red-light: #e8463a;
    --yellow: #fbd31a;
    --yellow-deep: #f5b90f;
    --navy: #17265c;
    --navy-deep: #0f1b45;
    --blue: #2a57a8;
    --white: #ffffff;
    --ink: #111111;
  }
  * { box-sizing: border-box; margin: 0; padding: 0; }
  html, body { width: 857px; height: 1200px; overflow: hidden; background: #fff; }
  .poster {
    position: relative; width: 857px; height: 1200px; overflow: hidden;
    font-family: "Open Sans", Arial, sans-serif; color: var(--white);
  }
  .backdrop { position: absolute; inset: 0; }
  .hero-figure {
    position: absolute; left: 470px; top: 125px; width: 350px; height: 545px;
    background: linear-gradient(180deg, #2c2c3a 0%, #2f4fa8 50%, #1d2f78 100%);
    border-radius: 170px 170px 40px 40px;
    opacity: 0.92;
  }
  .kicker, .headline, .title-right, .section-title, .profile-title {
    font-family: "Roboto Condensed", Arial, sans-serif;
  }
  .kicker {
    position: absolute; left: 44px; top: 22px;
    font-size: 34px; font-weight: 900; color: var(--white);
  }
  .headline {
    position: absolute; left: 40px; top: 52px;
    font-size: 72px; line-height: 1; font-weight: 900; font-style: italic;
    color: var(--white); text-shadow: 3px 3px 0 var(--red-deep);
  }
  .title-right {
    position: absolute; right: 26px; top: 18px; text-align: right;
    font-weight: 900; line-height: 1;
  }
  .title-right .line-1 { display: block; font-size: 42px; color: var(--ink); }
  .title-right .line-2 { display: block; font-size: 58px; color: var(--red); }
  .column { position: absolute; left: 44px; top: 134px; width: 410px; }
  .intro { font-size: 16.5px; line-height: 1.32; font-weight: 700; }
  .section-title {
    font-size: 25px; line-height: 1.04; font-weight: 900; color: var(--yellow);
    margin: 18px 0 8px;
  }
  .column p.body { font-size: 14.5px; line-height: 1.36; font-weight: 400; }
  .column p.narrow { width: 320px; }
  .profile-title {
    position: absolute; left: 380px; top: 640px; line-height: 0.92;
    font-style: italic; font-weight: 900; color: var(--white);
  }
  .profile-title .big { display: block; font-size: 62px; text-shadow: 3px 3px 0 var(--red); }
  .profile-title .small { display: block; font-size: 34px; color: var(--yellow); letter-spacing: 10px; padding-left: 4px; }
  .powers-lead {
    position: absolute; left: 300px; top: 728px; font-size: 17px; font-weight: 700;
  }
  .powers { position: absolute; top: 760px; list-style: none; }
  .powers li {
    position: relative; padding-left: 14px; font-size: 13px; line-height: 1.3; margin-bottom: 3px;
  }
  .powers li::before { content: ""; position: absolute; left: 0; top: 7px; width: 5px; height: 5px; border-radius: 50%; background: var(--yellow); }
  .powers.left { left: 44px; width: 310px; }
  .powers.right { left: 420px; width: 380px; }
  .join {
    position: absolute; left: 44px; top: 1030px; width: 600px;
    font-size: 27px; line-height: 1.2; font-weight: 700; color: var(--navy);
  }
  .join .join-us { color: var(--red); }
  .join .tag { color: var(--blue); }
  .brand {
    position: absolute; right: 36px; top: 1080px; display: flex; align-items: center; gap: 10px;
  }
  .brand-mark { width: 44px; height: 44px; border-radius: 50%; background: var(--navy); }
  .brand-name { font-size: 24px; font-weight: 700; color: var(--navy); }
</style>
</head>
<body>
<div class="poster">
  <svg class="backdrop" width="857" height="1200" viewBox="0 0 857 1200" aria-hidden="true">
    <rect width="857" height="1200" fill="var(--red)"/>
    <g fill="var(--red-light)">
      <polygon points="160,130 0,0 120,0"/>
      <polygon points="160,130 260,0 380,0"/>
      <polygon points="160,130 0,240 0,360"/>
      <polygon points="160,130 0,520 140,620"/>
      <polygon points="160,130 520,640 620,560"/>
    </g>
    <polygon points="520,0 857,0 857,700 640,560 460,140" fill="var(--yellow)"/>
    <polygon points="640,560 857,700 857,360" fill="var(--yellow-deep)"/>
    <path d="M0,700 C220,660 520,700 857,640 L857,1000 L0,1000 Z" fill="var(--navy)"/>
    <path d="M0,1000 C260,970 560,1005 857,975 L857,1200 L0,1200 Z" fill="var(--yellow)"/>
  </svg>

  <div class="hero-figure" role="img" aria-label="Illustration of a female superhero occupational therapist in a blue suit and cape with an OT chest emblem, hands on hips"></div>

  <div class="kicker">MEET YOUR LOCAL</div>
  <div class="headline">SUPERHERO</div>
  <div class="title-right"><span class="line-1">THE OCCUPATIONAL</span><span class="line-2">THERAPIST</span></div>

  <div class="column">
    <p class="intro">Imagine being defeated by an everyday task like putting your clothes on, catching a bus, spending time with your friends or taking care of yourself.</p>

    <h2 class="section-title">OCCUPATIONAL THERAPY<br>IS HERE TO HELP.</h2>
    <p class="body">The things that you do – your occupations – help express who you are, how you feel about yourself, and how you connect with others. Your health and wellbeing will be affected if you are unable to do the things you want and need to do, to live and enjoy your life.</p>

    <h2 class="section-title">OCCUPATIONAL THERAPISTS HELP<br>PEOPLE OF ALL AGES AND WORK<br>IN A VARIETY OF SETTINGS.</h2>
    <p class="body narrow">Occupations that could cause difficulty include preparing and eating meals; driving and mobility; recreation and exercise; use of a computer or workstation; showering or bathing; getting things done on time and in a preferred standard; having enough things to do and the confidence to do them; developing supportive relationships or friendships; or thriving in school.</p>
  </div>

  <div class="profile-title"><span class="big">SUPERHERO</span><span class="small">PROFILE</span></div>
  <div class="powers-lead">My super powers help people to:</div>

  <ul class="powers left">
    <li>Learn new ways of doing things following an illness or injury (e.g. dressing or cooking)</li>
    <li>Thrive in their senior years</li>
    <li>Regulate their strong emotions</li>
    <li>Achieve their goals at school</li>
    <li>Develop ways to manage pain</li>
    <li>Develop their confidence in social situations</li>
  </ul>
  <ul class="powers right">
    <li>Access support available in the community</li>
    <li>Adapt material or equipment (e.g. wheelchairs or provide a special bath or toilet seat)</li>
    <li>Make changes to their living or working environment</li>
    <li>Develop new skills, abilities or interests (e.g. job readiness programmes)</li>
  </ul>

  <div class="join">
    <span class="join-us">JOIN US</span> in celebrating occupational therapy by using the hashtag <span class="tag">#YourLocalSuperHero</span><br>
    Visit klrvptb.org.nz for more information
  </div>

  <div class="brand">
    <span class="brand-mark"></span>
    <span class="brand-name">KLRV-PTB</span>
  </div>
</div>
</body>
</html>
```